We'd like to rebrand The Ashvale Crafters & Bazaar to be a professional but community oriented market. This market will go from inside and outside, inviting locally made jewelry, clothing, house wares, knits, vintage and more. We always have buskers, coffee and dainties. This is a year- round market, so it has to work for Fall, Winter, Spring, Summer.
We'd like the words:
Local
Community
Music
and/or
Hand Made
Please, also make the dimensions 22x79.
This will a printed banner to hang at indoor and outdoor markets.
Adults in North America 20-55+
Average House-hold Budgets
House
Ashvale Crafters & Bazaar

```html
<!DOCTYPE html>
<html lang="en">
<head>
<meta charset="utf-8">
<title>Ashvale Crafters &amp; Bazaar — Banner</title>
<link rel="stylesheet" href="https://fonts.googleapis.com/css2?family=Tinos:wght@400;700&display=swap">
<style>
  :root {
    --banner-top: #6cc2a4;
    --banner-mid: #5ab898;
    --banner-bottom: #4fae8c;
    --ink-light: #f4f7f2;
    --notes-deep: #3f8d75;
    --notes-soft: #56a88c;
    --diamond: #eef3ee;
  }
  * { margin: 0; padding: 0; box-sizing: border-box; }
  html, body { width: 1200px; height: 4317px; overflow: hidden; }
  body { background: var(--banner-bottom); }
  .banner {
    position: relative;
    width: 1200px;
    height: 4317px;
    overflow: hidden;
    background: linear-gradient(180deg, var(--banner-top) 0%, var(--banner-mid) 45%, var(--banner-bottom) 100%);
    font-family: "Tinos", "Times New Roman", serif;
    color: var(--ink-light);
  }
  .music-notes-art {
    position: absolute;
    left: 60px;
    top: 60px;
    width: 1080px;
    height: 1120px;
    border-radius: 24px;
    background: linear-gradient(160deg, var(--notes-soft) 0%, var(--notes-deep) 55%, var(--notes-soft) 100%);
  }
  .brand {
    position: absolute;
    left: 0;
    width: 1200px;
    top: 1420px;
    text-align: center;
    font-weight: 700;
    color: var(--ink-light);
    text-transform: uppercase;
    line-height: 1.05;
  }
  .brand-line { display: block; }
  .brand-line-1 { font-size: 190px; letter-spacing: 6px; }
  .brand-line-2 { font-size: 130px; letter-spacing: 8px; margin-top: 20px; }
  .brand-line-3 { font-size: 150px; letter-spacing: 10px; margin-top: 20px; }
  .tagline {
    position: absolute;
    left: 0;
    width: 1200px;
    top: 2100px;
    text-align: center;
    font-size: 52px;
    font-weight: 700;
    color: var(--ink-light);
  }
  .value-word {
    position: absolute;
    left: 0;
    width: 1200px;
    text-align: center;
    line-height: 1;
    text-transform: uppercase;
  }
  .value-local { top: 2862px; font-size: 150px; font-weight: 400; letter-spacing: 4px; }
  .value-community { top: 3266px; font-size: 95px; font-weight: 400; letter-spacing: 2px; }
  .value-handmade { top: 3644px; font-size: 85px; font-weight: 700; letter-spacing: 1px; }
  .value-music { top: 4006px; font-size: 110px; font-weight: 700; letter-spacing: 3px; }
  .divider {
    position: absolute;
    left: 440px;
    width: 330px;
    height: 80px;
  }
  .divider-1 { top: 3077px; }
  .divider-2 { top: 3457px; }
  .divider-3 { top: 3832px; }
</style>
</head>
<body>
  <main class="banner">
    <div class="music-notes-art" role="img" aria-label="Scattered treble clefs, bass clefs and musical notes in deep teal"></div>

    <h1 class="brand" aria-label="Ashvale Crafters &amp; Bazaar">
      <span class="brand-line brand-line-1">Ashvale</span>
      <span class="brand-line brand-line-2">Crafters &amp;</span>
      <span class="brand-line brand-line-3">Bazaar</span>
    </h1>

    <p class="tagline">From community to community.</p>

    <p class="value-word value-local">Local</p>
    <svg class="divider divider-1" viewBox="0 0 330 80" aria-hidden="true">
      <g fill="var(--diamond)">
        <polygon points="48,6 82,40 48,74 14,40"/>
        <polygon points="165,6 199,40 165,74 131,40"/>
        <polygon points="285,6 319,40 285,74 251,40"/>
      </g>
    </svg>
    <p class="value-word value-community">Community</p>
    <svg class="divider divider-2" viewBox="0 0 330 80" aria-hidden="true">
      <g fill="var(--diamond)">
        <polygon points="48,6 82,40 48,74 14,40"/>
        <polygon points="165,6 199,40 165,74 131,40"/>
        <polygon points="285,6 319,40 285,74 251,40"/>
      </g>
    </svg>
    <p class="value-word value-handmade">Hand Made</p>
    <svg class="divider divider-3" viewBox="0 0 330 80" aria-hidden="true">
      <g fill="var(--diamond)">
        <polygon points="48,6 82,40 48,74 14,40"/>
        <polygon points="165,6 199,40 165,74 131,40"/>
        <polygon points="285,6 319,40 285,74 251,40"/>
      </g>
    </svg>
    <p class="value-word value-music">Music</p>
  </main>
</body>
</html>
```